VelgoNexus PowerPoint Design

We need a very cool power-point template done for VelgoNexus. We need it to drive the message of technology, speed and innovation. This is for a racing proposal to for our indy car team. I will attach our logo.

Target Market(s)

This presentation is for our INDY RACE CAR TEAM OVERVIEW... The Theme is: Speed, Technology and Innovation

Industry/Entity Type

Racing

Colors

Designer to choose colors to be used in the design.

Requirements
Must have
• Intro Slide with Logo - Must look very cool
Template Slide for Content
Ending Slide with something like "Thanks VelgoNexus!"
Nice to have
• Please see the example ppt deck from Morbeck a previous company to see the slide template... Also see a old template for VelgoNexus

```html
<!DOCTYPE html>
<html lang="en">
<head>
<meta charset="utf-8">
<title>VelgoNexus – Title Slide</title>
<link rel="stylesheet" href="https://fonts.googleapis.com/css2?family=Cabin:wght@500&family=Carlito&display=swap">
<style>
  :root {
    --navy: #061a4e;
    --glow: #17428c;
    --brand-blue: #3b7dc0;
    --title-blue: #3f88cc;
    --body-blue: #3a79c8;
    --divider: rgba(70, 120, 200, 0.35);
    --amber: rgba(224, 160, 42, 0.6);
  }
  * { margin: 0; padding: 0; box-sizing: border-box; }
  html, body {
    width: 1200px;
    height: 900px;
    overflow: hidden;
    background: var(--navy);
  }
  .slide {
    position: relative;
    width: 1200px;
    height: 900px;
    overflow: hidden;
    background: var(--navy);
  }
  .header-texture {
    position: absolute;
    left: 0; top: 0;
    width: 1200px;
    height: 420px;
    background:
      linear-gradient(180deg, var(--amber) 0px, rgba(170,120,50,0.35) 45px, rgba(23,66,140,0) 95px),
      radial-gradient(ellipse 75% 85% at 50% 10%, var(--glow) 0%, rgba(16,50,115,0.6) 45%, rgba(6,26,78,0) 100%);
  }
  .brand {
    position: absolute;
    left: 120px;
    top: 536px;
    width: 388px;
  }
  .brand-name {
    font-family: "Cabin", sans-serif;
    font-weight: 500;
    font-size: 54px;
    line-height: 1;
    color: var(--brand-blue);
    letter-spacing: 1px;
    padding-bottom: 7px;
    border-bottom: 2px solid var(--brand-blue);
  }
  .brand-tagline {
    margin-top: 6px;
    font-family: "Carlito", sans-serif;
    font-size: 17.5px;
    color: var(--brand-blue);
    white-space: nowrap;
  }
  .divider {
    position: absolute;
    left: 553px;
    top: 472px;
    width: 2px;
    height: 175px;
    background: linear-gradient(180deg, rgba(70,120,200,0) 0%, var(--divider) 30%, var(--divider) 70%, rgba(70,120,200,0) 100%);
  }
  .title-block {
    position: absolute;
    left: 607px;
    top: 478px;
    width: 470px;
  }
  .project-title {
    font-family: "Cabin", sans-serif;
    font-weight: 500;
    font-size: 50px;
    line-height: 1.1;
    color: var(--title-blue);
    letter-spacing: -0.3px;
    white-space: nowrap;
  }
  .project-summary {
    margin-top: 16px;
    font-family: "Carlito", sans-serif;
    font-size: 19.5px;
    line-height: 30px;
    color: var(--body-blue);
  }
</style>
</head>
<body>
  <main class="slide">
    <div class="header-texture" role="img" aria-label="Glowing blue light texture with a band of warm amber lights along the top edge"></div>

    <div class="brand">
      <div class="brand-name">VelgoNexus</div>
      <div class="brand-tagline">Speed, Technology and Innovation at Every Turn</div>
    </div>

    <div class="divider"></div>

    <section class="title-block">
      <h1 class="project-title">Project Title Here</h1>
      <p class="project-summary">Lorem ipsum dolor sit lorem ipsum dolor sit Lorem ipsum dolor sit lorem ipsum dolor sit Lorem ipsum dolor sit lorem ipsum dolor sit</p>
    </section>
  </main>
</body>
</html>
```